Verdant Rooms Stationary Set

Verdant Rooms is a bespoke interior design firm set to provide services to VIP clients with elegance and minimalism is the main theme for our stationary set. We require a full stationary set covering A4 letterhead, A4 & A3 envelopes, business cards, USB's, CDs, email signature and any other item the designer sees fit. logo is already designed and finalized, and we require the designer to use it as is without modifying the logo.

Address to be used on letterhead / business cards ...etc shall be as follows:

Phone : +971 2 518 3076
P.O. Box : 318947
Address: Block C&D, Bldg. 27, Court 14, Abu Dhabi, United Arab Emirates
Website: www.verdantrooms.example

Target Market(s)

VIP Clients

Industry/Entity Type

Interior Design

Font styles to use
Other font styles liked:
• something to be unique

Colors

Designer to choose colors to be used in the design.

Requirements
Must have
• Elegant, minimalistic
Nice to have
• Simple yet elegant design having a sharp yet clean cut format
Should not have
• No additional colours, just colours that are used in the logo (silver, black or gold)

```html
<!DOCTYPE html>
<html lang="en">
<head>
<meta charset="utf-8">
<title>Verdant Rooms – Business Card</title>
<link href="https://fonts.googleapis.com/css2?family=Cormorant+Garamond:wght@500&family=Montserrat:wght@400;500;700&display=swap" rel="stylesheet">
<style>
  :root {
    --backdrop: #dedddb;
    --paper: #ffffff;
    --gold: #b0924f;
    --silver: #7f8084;
    --black: #201e1f;
    --ink: #2b2b2b;
  }
  html, body {
    margin: 0;
    padding: 0;
    width: 1200px;
    height: 810px;
    overflow: hidden;
    background: var(--backdrop);
  }
  .canvas {
    position: relative;
    width: 1200px;
    height: 810px;
  }
  .card {
    position: absolute;
    top: 250px;
    width: 520px;
    height: 300px;
    overflow: hidden;
    box-shadow: 0 6px 18px rgba(0,0,0,0.18);
  }
  .card--front { left: 55px; background: var(--paper); }
  .card--back { left: 625px; background: var(--black); }

  .card__swoosh { position: absolute; inset: 0; }

  .wordmark {
    position: absolute;
    font-family: "Cormorant Garamond", Georgia, serif;
    font-weight: 500;
    color: var(--gold);
    letter-spacing: 0.06em;
    white-space: nowrap;
  }
  .card--front .wordmark { left: 40px; top: 120px; font-size: 28px; }
  .card--back .wordmark {
    left: 0; right: 0; top: 118px;
    text-align: center;
    font-size: 48px;
  }

  .holder {
    position: absolute;
    left: 40px;
    bottom: 40px;
    font-family: "Montserrat", Arial, sans-serif;
  }
  .holder__name {
    margin: 0;
    font-size: 15px;
    font-weight: 700;
    color: var(--gold);
  }
  .holder__title {
    margin: 2px 0 0;
    font-size: 11px;
    font-weight: 500;
    color: var(--ink);
  }

  .contact {
    position: absolute;
    right: 20px;
    top: 60px;
    margin: 0;
    padding: 0;
    list-style: none;
    text-align: right;
    font-family: "Montserrat", Arial, sans-serif;
    font-size: 10px;
    line-height: 1.5;
    color: var(--paper);
    white-space: nowrap;
  }
  .contact__item { display: flex; justify-content: flex-end; align-items: center; gap: 6px; }
  .contact__item svg { width: 9px; height: 9px; flex: none; }
  .contact__address { margin-top: 8px; padding-right: 15px; }
</style>
</head>
<body>
<main class="canvas">

  <section class="card card--front" aria-label="Business card front">
    <svg class="card__swoosh" viewBox="0 0 520 300" preserveAspectRatio="none" aria-hidden="true">
      <path d="M300 0 C345 30 320 160 160 300 L176 300 C338 162 362 30 314 0 Z" fill="var(--silver)"/>
      <path d="M318 0 C366 30 342 164 180 300 L520 300 L520 0 Z" fill="var(--gold)"/>
    </svg>

    <div class="wordmark">Verdant Rooms</div>

    <div class="holder">
      <p class="holder__name">Samir Haddad</p>
      <p class="holder__title">Managing Director</p>
    </div>

    <ul class="contact">
      <li class="contact__item">+971 2 518 3076
        <svg viewBox="0 0 10 10"><circle cx="5" cy="5" r="5" fill="var(--paper)"/><path d="M3 2.5l1 1-0.6 0.8a3 3 0 0 0 2.3 2.3l0.8-0.6 1 1-0.8 0.8A4.5 4.5 0 0 1 2.2 3.3Z" fill="var(--gold)"/></svg>
      </li>
      <li class="contact__item">info@verdantrooms.example
        <svg viewBox="0 0 10 10"><rect x="0.5" y="2" width="9" height="6" fill="none" stroke="var(--paper)"/><path d="M0.5 2l4.5 3.5L9.5 2" fill="none" stroke="var(--paper)"/></svg>
      </li>
      <li class="contact__item">www.verdantrooms.example
        <svg viewBox="0 0 10 10"><circle cx="5" cy="5" r="4.5" fill="none" stroke="var(--paper)"/><path d="M0.5 5h9M5 0.5c-2.4 2.6-2.4 6.4 0 9M5 0.5c2.4 2.6 2.4 6.4 0 9" fill="none" stroke="var(--paper)" stroke-width="0.8"/></svg>
      </li>
      <li class="contact__address">P.O. Box : 318947<br>Block C&amp;D, Bldg. 27, Court 14<br>Abu Dhabi, United Arab Emirates</li>
    </ul>
  </section>

  <section class="card card--back" aria-label="Business card back">
    <div class="wordmark">Verdant Rooms</div>
  </section>

</main>
</body>
</html>
```